Business Card Design Competition

We need a business card design for our Internet Marketing company. We require both front and back designs and the final card must be 89x53mm in size, plus crop marks to 91x55mm. Colours as per logo, plus perhaps black and/or grey (#828282).
Final text must be editable (if you can supply an editable Fireworks PNG, even better)...
FRONT TEXT:
Full Name
Position
Address Line
Suburb, State, Postcode
Phone: 0000 000 000
Mobile: 0000 000 000
Email: xxx@brimleafpromo.com.au
Web: www.brimleafpromo.com.au
Rear of card should be a fresh design plus our slogan text: "Putting You Forward" in large font, then in small text "Brimleaf Holdings Pty Ltd (ABN: 42 563 701 384)".
Target Market(s)
Small/Medium Businesses
Industry/Entity Type
Business
Look and feel
Each slider illustrates characteristics of the customer's brand and the style your logo design should communicate.

```html
<!DOCTYPE html>
<html lang="en">
<head>
<meta charset="UTF-8">
<title>Brimleaf Promo – Business Cards</title>
<link href="https://fonts.googleapis.com/css2?family=Varela+Round&family=Tinos:wght@400;700&family=Montserrat:wght@500;700&display=swap" rel="stylesheet">
<style>
  :root {
    --bg: #e9e9e9;
    --card-dark: #1d1d1d;
    --card-light: #fbfbf9;
    --orange: #f08a1c;
    --green: #8dc63f;
    --grey: #828282;
    --ink: #3a3a3a;
    --navy: #1f3a5f;
    --legal: #cfcfcf;
  }
  * { margin: 0; padding: 0; box-sizing: border-box; }
  html, body { width: 1200px; height: 902px; overflow: hidden; }
  body { background: var(--bg); position: relative; font-family: "Varela Round", sans-serif; }

  .card {
    position: absolute;
    width: 680px;
    height: 405px;
    overflow: hidden;
    box-shadow: 0 6px 18px rgba(0,0,0,0.18);
  }

  /* Rear card */
  .card--rear { left: 110px; top: 28px; background: var(--card-dark); }
  .rear-brand {
    position: absolute; left: 70px; top: 128px;
    display: flex; align-items: center; gap: 18px;
  }
  .brand-dot {
    flex: none;
    width: 84px; height: 84px; border-radius: 50%;
    border: 7px solid var(--green);
  }
  .rear-brand-text { display: flex; flex-direction: column; }
  .brand-name { color: var(--green); font-size: 40px; line-height: 1.05; white-space: nowrap; }
  .slogan { color: var(--orange); font-size: 40px; line-height: 1.15; margin-top: 4px; white-space: nowrap; }
  .rear-legal {
    position: absolute; right: 70px; bottom: 62px;
    color: var(--legal); font-size: 12px; font-family: "Montserrat", sans-serif; font-weight: 500;
  }

  /* Front card */
  .card--front { left: 410px; top: 468px; background: var(--card-light); }
  .front-deco {
    position: absolute; right: 150px; top: 28px;
    width: 118px; height: 118px; border-radius: 50%;
    border: 10px solid rgba(141,198,63,0.14);
    background: rgba(240,138,28,0.06);
  }
  .contact {
    position: absolute; left: 62px; top: 128px;
    font-family: "Tinos", serif; color: var(--ink);
    font-size: 17px; line-height: 1.28; list-style: none;
  }
  .contact .web { color: var(--green); font-weight: 700; }
  .front-brand {
    position: absolute; left: 62px; top: 270px;
    display: flex; align-items: center; gap: 10px;
  }
  .front-brand .brand-dot { width: 38px; height: 38px; border-width: 4px; }
  .front-brand .brand-name { font-size: 24px; }
  .person {
    position: absolute; right: 52px; top: 168px;
    font-family: "Montserrat", sans-serif;
  }
  .person-name { color: var(--navy); font-weight: 700; font-size: 20px; letter-spacing: 0.5px; }
  .person-role { color: var(--grey); font-weight: 500; font-size: 8.5px; letter-spacing: 3px; margin-top: 2px; }
  .front-band {
    position: absolute; left: 0; right: 0; top: 326px; height: 20px;
    background: var(--green);
  }
</style>
</head>
<body>
  <section class="card card--rear">
    <div class="rear-brand">
      <div class="brand-dot"></div>
      <div class="rear-brand-text">
        <span class="brand-name">Brimleaf Promo</span>
        <span class="slogan">Putting You Forward</span>
      </div>
    </div>
    <p class="rear-legal">Brimleaf Holdings Pty Ltd (ABN: 42 563 701 384)</p>
  </section>

  <section class="card card--front">
    <div class="front-deco"></div>
    <ul class="contact">
      <li>Address Line</li>
      <li>Suburb, State, Postcode</li>
      <li>Phone: 0000 000 000</li>
      <li>Mobile: 0000 000 000</li>
      <li>Email: xxx@brimleafpromo.com.au</li>
      <li class="web">www.brimleafpromo.com.au</li>
    </ul>
    <div class="front-brand">
      <div class="brand-dot"></div>
      <span class="brand-name">Brimleaf Promo</span>
    </div>
    <div class="person">
      <p class="person-name">LIAM CORBETT</p>
      <p class="person-role">NETWORK CONSULTANT</p>
    </div>
    <div class="front-band"></div>
  </section>
</body>
</html>
```